inspirational business card

I want to use the Vector on Pixavend.com (number 58172046) and I will purchase the vector to send it to the designer once the general concept is approved. You can download it for free for a one time use on providing a design for this request.
Within the vector, insert:
Tessa Brundle
Guidance and Partnering

I prefer a vertical card but do not require vertical.

Contact info:

Tessa Brundle, J.D.
Collaborative Lawyer
Certified Divorce Coach
Mediation Coach
PHONE 515/555-0143
EMAIL: tbjd@quellmail.net

Website: Guidanceandpartnering.com
Settlementcourse.com

I like greens, blue and grey. I do not want black font, and would like the font to be legible without needing perfect reading vision (no super small font).
I would like the overall theme to convey growth and nurturance.
I like the vector I selected because of the growth and light portrayed.
Not too frilly or too bold. I would like to to appeal to both sexes.

Target Market(s)

Generally professional women 35-60

Industry/Entity Type

Attorney

Font styles to use
Serif
Sans Serif

Colors
acd136
cadf82
fbf289
9d9d9d

Requirements
Must have
• My project does not need to have my photo but you could use it if you want
Nice to have
• Vertical
• I like rounded edges on the cards
Should not have
• I do not like my name appearing two times in close proximity. I'm not a flowery person.

```html
<!DOCTYPE html>
<html lang="en">
<head>
<meta charset="utf-8">
<title>Tessa Brundle, J.D. — Business Card</title>
<link rel="stylesheet" href="https://fonts.googleapis.com/css2?family=Roboto:wght@300;400&display=swap">
<style>
  :root {
    --page-bg: #e6e7e9;
    --teal: #13afd3;
    --teal-soft: #5cbdd8;
    --white: #ffffff;
  }
  * { margin: 0; padding: 0; box-sizing: border-box; }
  html, body { width: 747px; height: 1200px; overflow: hidden; }
  body {
    background: var(--page-bg);
    font-family: "Roboto", Arial, sans-serif;
    position: relative;
  }
  .card {
    position: absolute;
    top: 37px;
    width: 291px;
    height: 466px;
    border-radius: 17px;
    overflow: hidden;
  }
  .card--front { left: 53px; background: var(--white); }
  .card--back  { left: 402px; background: var(--teal); }

  .tree-art {
    position: absolute;
    border-radius: 50%;
  }
  .card--front .tree-art {
    left: 70px; top: 23px; width: 150px; height: 150px;
    background: radial-gradient(circle at 50% 40%, #7fd0e6 0%, var(--teal) 70%);
  }
  .card--back .tree-art {
    left: 45px; top: 135px; width: 200px; height: 200px;
    background: radial-gradient(circle at 50% 40%, #ffffff 0%, #c9eef7 55%, #8fd8ec 100%);
  }

  .front-band { position: absolute; left: 0; top: 200px; width: 291px; height: 266px; }

  .identity {
    position: absolute; right: 36px; top: 257px;
    text-align: right; color: var(--white);
  }
  .identity__name { font-size: 24px; font-weight: 400; line-height: 1.1; margin-bottom: 3px; }
  .identity__role { font-size: 13px; font-weight: 300; line-height: 1.15; }

  .contacts { position: absolute; left: 46px; top: 345px; list-style: none; color: var(--white); }
  .contacts__item {
    display: flex; align-items: flex-start;
    margin-bottom: 16px;
    font-size: 13px; font-weight: 300; line-height: 16px;
  }
  .contacts__item:last-child { margin-bottom: 0; }
  .contacts__icon {
    width: 24px; height: 24px; border-radius: 50%;
    border: 1.5px solid var(--white);
    flex: none; margin-right: 11px; margin-top: -4px;
    display: flex; align-items: center; justify-content: center;
  }
  .contacts__icon--web { background: var(--white); color: var(--teal); font-size: 7px; font-weight: 400; }

  .brand {
    position: absolute; left: 0; top: 0; width: 291px; height: 466px;
  }
  .brand__name { font-family: "Roboto", Arial, sans-serif; font-weight: 400; fill: var(--teal); font-size: 12px; }
  .brand__tagline { font-family: "Roboto", Arial, sans-serif; font-weight: 400; fill: var(--white); font-size: 8.5px; }
</style>
</head>
<body>

<section class="card card--front" aria-label="Card front">
  <div class="tree-art" role="img" aria-label="Tree of growth illustration in a crescent frame"></div>

  <svg class="front-band" viewBox="0 0 291 266" aria-hidden="true">
    <path d="M0 20 C70 5 110 -8 170 2 C220 10 260 18 291 24 L291 266 L0 266 Z" fill="var(--teal-soft)"/>
    <path d="M0 42 C70 25 110 14 170 22 C220 28 260 36 291 42 L291 266 L0 266 Z" fill="var(--teal)"/>
  </svg>

  <div class="identity">
    <p class="identity__name">Tessa Brundle, J.D.</p>
    <p class="identity__role">Collaborative Lawyer</p>
    <p class="identity__role">Certified Divorce Coach</p>
    <p class="identity__role">Mediation Coach</p>
  </div>

  <ul class="contacts">
    <li class="contacts__item">
      <span class="contacts__icon">
        <svg width="12" height="12" viewBox="0 0 24 24" aria-hidden="true"><path fill="#fff" d="M6.6 10.8a15 15 0 0 0 6.6 6.6l2.2-2.2c.3-.3.7-.4 1-.2 1.1.4 2.3.6 3.6.6.6 0 1 .4 1 1V20c0 .6-.4 1-1 1A17 17 0 0 1 3 4c0-.6.4-1 1-1h3.5c.6 0 1 .4 1 1 0 1.3.2 2.5.6 3.6.1.3 0 .7-.2 1z"/></svg>
      </span>
      <span>515/555-0143</span>
    </li>
    <li class="contacts__item">
      <span class="contacts__icon">
        <svg width="12" height="9" viewBox="0 0 24 18" aria-hidden="true"><rect x="1" y="1" width="22" height="16" rx="1" fill="none" stroke="#fff" stroke-width="2"/><path d="M1 1 L12 10 L23 1" fill="none" stroke="#fff" stroke-width="2"/></svg>
      </span>
      <span>tbjd@quellmail.net</span>
    </li>
    <li class="contacts__item">
      <span class="contacts__icon contacts__icon--web">www</span>
      <span>guidanceandpartnering.com<br>settlementcourse.com</span>
    </li>
  </ul>
</section>

<section class="card card--back" aria-label="Card back">
  <div class="tree-art" role="img" aria-label="Tree of growth illustration in a crescent frame"></div>
  <svg class="brand" viewBox="0 0 291 466" aria-label="Tessa Brundle — Guidance and Partnering">
    <defs>
      <path id="tagline-arc" d="M52 320 A108 108 0 0 0 240 320"/>
    </defs>
    <text class="brand__name" x="150" y="290" text-anchor="middle">Tessa</text>
    <text class="brand__name" x="150" y="304" text-anchor="middle">Brundle</text>
    <text class="brand__tagline"><textPath href="#tagline-arc" startOffset="50%" text-anchor="middle">Guidance and Partnering</textPath></text>
  </svg>
</section>

</body>
</html>
```